Business Card Design Project

Looking for a logo and business card for a Real State Business i will be opening. The name is not choosen yet , but will probably be RTV IMOVEIS.
I was thinking black and silver colors, but am open to nice ideas.
I did add a business card that i liked a lot, am looking for something like that, with logo in black or silver in a black card. The logo i was thinking in the letters RTV as i uploaded or something or little and cute buildings or a house...just ideas, can be any nice logo.
Updates

You guys can add other colors if you want, I like colors very "BRIGHT" and "open", like red, pink, strong colors. almost glow in the dark colors. lol

Designers,

I've increased more 88 dollars in the budget for 1st place cause I will want envelope designs... small and big sizes.

So 1st place is now U$248,00. 

No need to send the envelope designs right now... only the business cards designs.

Thank you.

Industry/Entity Type

Business

Requirements
Must have
• Renata Tavares Vilela

www.RTVimoveis-exemplo.com.br

+554188316402

renata@rtvimoveis-exemplo.com.br

```html
<!DOCTYPE html>
<html lang="pt-BR">
<head>
<meta charset="utf-8">
<title>RTV Imóveis – Cartão de Visita</title>
<link rel="stylesheet" href="https://fonts.googleapis.com/css2?family=Arimo:wght@400&family=Cormorant+Garamond:ital,wght@0,500;1,500&display=swap">
<style>
  :root {
    --card-top: #262626;
    --card-mid: #1c1c1c;
    --card-bottom: #111111;
    --glow: rgba(255, 255, 255, 0.07);
    --silver: #d4d4d4;
    --text: #f2f2f2;
  }
  html, body {
    margin: 0;
    padding: 0;
    width: 686px;
    height: 1200px;
    overflow: hidden;
    background: var(--card-bottom);
  }
  .card {
    position: relative;
    width: 686px;
    height: 1200px;
    overflow: hidden;
    background: linear-gradient(180deg, var(--card-top) 0%, var(--card-mid) 55%, var(--card-bottom) 100%);
  }
  .card__texture {
    position: absolute;
    inset: 0;
    background: radial-gradient(ellipse 70% 45% at 50% 35%, var(--glow) 0%, rgba(255, 255, 255, 0) 100%);
  }
  .brand-mark {
    position: absolute;
    top: 250px;
    left: 0;
    width: 100%;
    margin: 0;
    text-align: center;
    font-family: "Cormorant Garamond", "Times New Roman", serif;
    font-style: normal;
    font-weight: 500;
    font-size: 220px;
    line-height: 1;
    letter-spacing: 4px;
    color: var(--silver);
  }
  .holder-name {
    position: absolute;
    top: 758px;
    left: 0;
    width: 100%;
    margin: 0;
    text-align: center;
    font-family: "Cormorant Garamond", "Times New Roman", serif;
    font-style: italic;
    font-weight: 500;
    font-size: 48px;
    line-height: 1.2;
    color: var(--text);
  }
  .contact {
    position: absolute;
    left: 0;
    width: 100%;
    margin: 0;
    text-align: center;
    font-family: "Arimo", Arial, sans-serif;
    font-weight: 400;
    line-height: 1.2;
    color: var(--text);
  }
  .contact--web { top: 886px; font-size: 34px; }
  .contact--phone { top: 938px; font-size: 56px; letter-spacing: 1px; }
  .contact--mail { top: 1022px; font-size: 30px; }
</style>
</head>
<body>
  <main class="card">
    <div class="card__texture" role="img" aria-label="Faint pattern of thin light lines crossing the dark card background"></div>

    <div class="brand-mark">RTV</div>

    <h1 class="holder-name">Renata Tavares Vilela</h1>

    <p class="contact contact--web">www.RTVimoveis-exemplo.com.br</p>
    <p class="contact contact--phone">+554188316402</p>
    <p class="contact contact--mail">renata@rtvimoveis-exemplo.com.br</p>
  </main>
</body>
</html>
```